Harbor Lantern Business Card
remarkable business card
Project: Harbor Lantern Business Card
Harbor Lantern Business Card - Events
Creative Brief
Use specific fonts
Use the fonts in my logo and/or the fonts that look best
Bright & Fun-filled
Tom Vesk
Culture Director
not to be listed on the card
Vesk@HarborLantern.example
www.HarborLantern.example
I want the Name to be prominent . I don't want the address to be listed This should be a very remarkable card. It needs to get instant attention that people will remember, and talk about. People should say wow! you need to see this card. That is a great looking card!

```html
<!DOCTYPE html>
<html lang="en">
<head>
<meta charset="utf-8">
<title>Harbor Lantern Stationery</title>
<link href="https://fonts.googleapis.com/css2?family=Open+Sans:wght@400;600;700&display=swap" rel="stylesheet">
<style>
  :root {
    --stage: #ebe6df;
    --paper: #ffffff;
    --ink: #4a4a4a;
    --muted: #8a8a8a;
    --brand: #5f9b2e;
    --night: #151515;
    --blue: #1f5fc4;
    --blue-deep: #0f3c8c;
    --rule: #d9d9d9;
    --accent-a: #e8553e;
    --accent-b: #3a8fd6;
  }
  * { box-sizing: border-box; margin: 0; padding: 0; }
  html, body { width: 1200px; height: 437px; overflow: hidden; }
  body {
    position: relative;
    background: var(--stage);
    font-family: "Open Sans", sans-serif;
    color: var(--ink);
  }
  .piece { position: absolute; }
  .caption {
    position: absolute;
    font-size: 5px;
    color: var(--muted);
    white-space: nowrap;
    transform: translateX(-50%);
  }

  /* brand lockup */
  .wordmark {
    display: flex; align-items: center; gap: 5px;
    font-weight: 700; color: var(--brand); white-space: nowrap; line-height: 1;
  }
  .wordmark .dot { border-radius: 50%; background: var(--brand); flex: none; }

  .intro { left: 20px; top: 96px; width: 170px; }
  .intro .wordmark { font-size: 15px; }
  .intro .wordmark .dot { width: 14px; height: 14px; }
  .intro .title { margin-top: 14px; padding-left: 40px; font-size: 5px; color: var(--muted); }

  /* business cards */
  .card {
    width: 163px; height: 94px; padding: 12px 12px;
    box-shadow: 0 1px 3px rgba(0,0,0,.25);
  }
  .card .wordmark { font-size: 11px; gap: 4px; }
  .card .wordmark .dot { width: 10px; height: 10px; }
  .card .details { margin-top: 14px; font-size: 4.5px; line-height: 1.55; }
  .card .name { font-weight: 700; font-size: 5.5px; }
  .card-dark { left: 24px; top: 175px; background: var(--night); color: #ddd; }
  .card-light { left: 24px; top: 295px; background: var(--paper); }
  .card .edge {
    position: absolute; right: 0; top: 0; bottom: 0; width: 5px; background: var(--blue);
  }

  /* letterheads */
  .letterhead {
    top: 24px; width: 197px; height: 365px; background: var(--paper);
    box-shadow: 0 1px 4px rgba(0,0,0,.2); padding: 10px 12px;
  }
  .letterhead-one { left: 199px; }
  .letterhead-two { left: 432px; }
  .letterhead .head { display: flex; justify-content: space-between; align-items: flex-start; }
  .letterhead .wordmark { font-size: 10px; gap: 3px; }
  .letterhead .wordmark .dot { width: 9px; height: 9px; }
  .letterhead .contact { font-size: 3.4px; line-height: 1.6; color: var(--muted); }
  .letterhead .side-tab {
    position: absolute; left: -3px; top: 28px; width: 4px; height: 18px; background: var(--blue);
  }
  .letterhead .foot {
    position: absolute; left: 12px; right: 12px; bottom: 8px;
    border-top: 1px solid var(--rule); padding-top: 3px;
    font-size: 3.4px; color: var(--muted); text-align: center; white-space: nowrap;
  }

  /* envelopes */
  .envelope { width: 360px; height: 90px; box-shadow: 0 1px 4px rgba(0,0,0,.25); overflow: hidden; }
  .envelope svg { position: absolute; inset: 0; }
  .envelope-dark { left: 828px; top: 24px; width: 355px; background: var(--night); }
  .envelope-blue { left: 828px; top: 89px; height: 72px; background: linear-gradient(180deg, var(--blue), var(--blue-deep)); }
  .envelope-white { left: 828px; top: 175px; height: 89px; background: var(--paper); }
  .envelope-front { left: 806px; top: 257px; width: 346px; height: 108px; background: var(--paper); }
  .envelope .seal {
    position: absolute; left: 50%; top: 12px; transform: translateX(-50%);
    width: 9px; height: 9px; border-radius: 50%; background: var(--paper);
  }
  .envelope-front .wordmark { position: absolute; left: 8px; top: 10px; font-size: 11px; gap: 4px; }
  .envelope-front .wordmark .dot { width: 10px; height: 10px; }
  .envelope-front .sender { position: absolute; left: 22px; top: 26px; font-size: 3.6px; color: var(--muted); }
</style>
</head>
<body>

  <section class="piece intro">
    <div class="wordmark"><span class="dot"></span>Harbor Lantern</div>
    <p class="title">Stationery Concepts</p>
  </section>

  <article class="piece card card-dark">
    <div class="wordmark"><span class="dot"></span>Harbor Lantern</div>
    <div class="details">
      <p class="name">Tom Vesk</p>
      <p>Culture Director</p>
      <p>Vesk@HarborLantern.example</p>
      <p>www.HarborLantern.example</p>
    </div>
    <span class="edge"></span>
  </article>
  <p class="caption" style="left:105px;top:279px;">Business Card Option 1</p>

  <article class="piece card card-light">
    <div class="wordmark"><span class="dot"></span>Harbor Lantern</div>
    <div class="details">
      <p class="name">Tom Vesk</p>
      <p>Culture Director</p>
      <p>Vesk@HarborLantern.example</p>
      <p>www.HarborLantern.example</p>
    </div>
    <span class="edge"></span>
  </article>
  <p class="caption" style="left:105px;top:401px;">Business Card Option 2</p>

  <article class="piece letterhead letterhead-one">
    <div class="head">
      <div class="wordmark"><span class="dot"></span>Harbor Lantern</div>
      <div class="contact">
        <p>Tom Vesk</p>
        <p>Vesk@HarborLantern.example</p>
        <p>www.HarborLantern.example</p>
      </div>
    </div>
    <span class="side-tab"></span>
    <p class="foot">www.HarborLantern.example</p>
  </article>
  <p class="caption" style="left:297px;top:403px;">Letterhead Option 1</p>

  <article class="piece letterhead letterhead-two">
    <div class="head">
      <div class="wordmark"><span class="dot"></span>Harbor Lantern</div>
    </div>
    <span class="side-tab"></span>
    <p class="foot">Tom Vesk &nbsp;|&nbsp; Vesk@HarborLantern.example &nbsp;|&nbsp; www.HarborLantern.example</p>
  </article>
  <p class="caption" style="left:530px;top:403px;">Letterhead Option 2</p>

  <div class="piece envelope envelope-dark">
    <svg width="355" height="90" viewBox="0 0 355 90"><path d="M0 0 L177 40 L355 0" fill="none" stroke="#333" stroke-width="1"/></svg>
    <span class="seal"></span>
  </div>

  <div class="piece envelope envelope-blue">
    <svg width="360" height="72" viewBox="0 0 360 72"><path d="M0 0 L180 36 L360 0" fill="none" stroke="#4b82dc" stroke-width="1"/></svg>
    <span class="seal"></span>
  </div>

  <div class="piece envelope envelope-white">
    <svg width="360" height="89" viewBox="0 0 360 89"><path d="M0 0 L180 40 L360 0" fill="none" stroke="#e2e2e2" stroke-width="1"/></svg>
  </div>

  <div class="piece envelope envelope-front">
    <div class="wordmark"><span class="dot"></span>Harbor Lantern</div>
    <p class="sender">www.HarborLantern.example</p>
  </div>
  <p class="caption" style="left:996px;top:382px;">Envelope Front And Back</p>

</body>
</html>
```